New website

We ned to create a new website that reflects more who we are. We are delivering exclusive premium products to our customers and the current website does not reflect our products at all.
We believe in less is more and need a webpage that is clean yet professional and exclusive.

Target Market(s)

Dentistry

Industry/Entity Type

Dental

Number of Pages Required

5+ page

Font styles to use
Sans Serif

Colors

Designer to choose colors to be used in the design.

Requirements
Must have
• Picture gallery
• Nice structure
• Clean layout
Nice to have
• Light fonts
Should not have
• Any italic font styles

```html
<!DOCTYPE html>
<html lang="en">
<head>
<meta charset="UTF-8">
<title>Lumadent – Why choose us &amp; Team</title>
<link href="https://fonts.googleapis.com/css2?family=Montserrat:wght@400;500;600;700&display=swap" rel="stylesheet">
<style>
  :root {
    --red: #e31b3a;
    --blue: #0a5ea8;
    --green: #449c6b;
    --green-bright: #3aa34f;
    --green-pale: #a9d9b8;
    --ink: #1f1f1f;
    --body: #333333;
    --panel: #f5f5f5;
    --white: #ffffff;
  }
  * { margin: 0; padding: 0; box-sizing: border-box; }
  html, body { width: 1200px; height: 1200px; overflow: hidden; }
  body { position: relative; font-family: 'Montserrat', sans-serif; background: var(--white); color: var(--body); }

  .why { position: absolute; left: 0; top: 0; width: 1200px; height: 420px; background: var(--panel); overflow: hidden; }
  .why__title { position: absolute; left: 206px; top: -8px; font-size: 38px; font-weight: 700; color: var(--red); line-height: 1.2; }
  .why__photo { position: absolute; left: 673px; top: 0; width: 527px; height: 420px;
    background: linear-gradient(120deg, #6e5a48 0%, #b9a98e 35%, #c7c46a 55%, #8b6c4d 80%, #5c4636 100%); }
  .reason { position: absolute; left: 173px; width: 460px; }
  .reason__num { position: absolute; left: 0; top: 0; width: 21px; height: 21px; border-radius: 50%;
    background: var(--blue); color: var(--white); font-size: 13px; font-weight: 600; text-align: center; line-height: 21px; }
  .reason__title { position: absolute; left: 33px; top: 2px; font-size: 13.5px; font-weight: 500; color: var(--ink); white-space: nowrap; }
  .reason__text { position: absolute; left: 33px; top: 31px; width: 430px; font-size: 12px; line-height: 21px; color: var(--body); }

  .team { position: absolute; left: 0; top: 420px; width: 1200px; height: 593px; }
  .eyebrow { position: absolute; left: 0; width: 100%; text-align: center; font-size: 19px; font-weight: 600; letter-spacing: 2.5px; }
  .eyebrow::before { content: ""; display: inline-block; width: 24px; height: 2px; background: currentColor; vertical-align: middle; margin-right: 12px; opacity: .85; }
  .team__eyebrow { top: 82px; color: var(--blue); }
  .section-title { position: absolute; left: 0; width: 100%; text-align: center; font-size: 38px; font-weight: 700; }
  .team__title { top: 138px; color: var(--red); }
  .team__side { position: absolute; left: 1164px; top: 148px; writing-mode: vertical-rl; font-size: 14px; letter-spacing: 5px; color: #e9e9e9; }
  .arrow { position: absolute; top: 312px; }
  .arrow--prev { left: 37px; }
  .arrow--next { left: 1150px; }
  .member { position: absolute; top: 224px; width: 198px; }
  .member__photo { width: 198px; height: 197px; box-shadow: 0 6px 14px rgba(0,0,0,.08); }
  .member__name { margin-top: 36px; font-size: 13.5px; font-weight: 500; letter-spacing: 2px; color: var(--ink); }
  .member__rule { width: 12px; height: 2px; background: var(--green-bright); margin-top: 8px; }
  .member__role { margin-top: 9px; font-size: 14px; color: var(--body); }

  .testimonials { position: absolute; left: 0; top: 1013px; width: 1200px; height: 187px; background: var(--green); }
  .testimonials__eyebrow { top: 77px; color: var(--green-pale); }
  .testimonials__title { top: 117px; color: var(--white); }
</style>
</head>
<body>

<section class="why">
  <h2 class="why__title">Why choose us</h2>

  <div class="reason" style="top:63px">
    <span class="reason__num">1</span>
    <h3 class="reason__title">QUISQUE EFFICITUR CONGUE PRETIUM</h3>
    <p class="reason__text">Quisque efficitur congue pretium. Nunc suscipit augue sollicitudin trist ique rhoncus. Aliquam vitae felis odio. Donec sapien purus.</p>
  </div>
  <div class="reason" style="top:164px">
    <span class="reason__num">2</span>
    <h3 class="reason__title">PRAESENT ULTRICES ERAT URNA</h3>
    <p class="reason__text">Quisque efficitur congue pretium. Nunc suscipit augue sollicitudin trist ique rhoncus. Aliquam vitae felis odio. Donec sapien purus.</p>
  </div>
  <div class="reason" style="top:264px">
    <span class="reason__num">3</span>
    <h3 class="reason__title">NUNC A ODIO QUIS SAPIEN COMMODO CURSUS</h3>
    <p class="reason__text">Quisque efficitur congue pretium. Nunc suscipit augue sollicitudin trist ique rhoncus. Aliquam vitae felis odio. Donec sapien purus.</p>
  </div>

  <div class="why__photo" role="img" aria-label="Warehouse worker in a safety vest scanning a parcel"></div>
</section>

<section class="team">
  <p class="eyebrow team__eyebrow">OUR TEAM</p>
  <h2 class="section-title team__title">Meet the Lumadent Team</h2>
  <span class="team__side">OUR TEAM</span>

  <svg class="arrow arrow--prev" width="14" height="22" viewBox="0 0 14 22" aria-hidden="true"><path d="M12 2 L3 11 L12 20" fill="none" stroke="#3aa34f" stroke-width="1.5"/></svg>
  <svg class="arrow arrow--next" width="14" height="22" viewBox="0 0 14 22" aria-hidden="true"><path d="M2 2 L11 11 L2 20" fill="none" stroke="#3aa34f" stroke-width="1.5"/></svg>

  <article class="member" style="left:172px">
    <div class="member__photo" role="img" aria-label="Portrait of John Doe" style="background:linear-gradient(160deg,#4a4a4a,#2e2e2e 60%,#6a6a6a)"></div>
    <h3 class="member__name">JOHN DOE</h3>
    <div class="member__rule"></div>
    <p class="member__role">Curabitur metus ligula</p>
  </article>
  <article class="member" style="left:392px">
    <div class="member__photo" role="img" aria-label="Portrait of Hilary Doe" style="background:linear-gradient(160deg,#3c3c3c,#5a4a42 55%,#6b6f86)"></div>
    <h3 class="member__name">HILARY DOE</h3>
    <div class="member__rule"></div>
    <p class="member__role">Curabitur metus ligula</p>
  </article>
  <article class="member" style="left:611px">
    <div class="member__photo" role="img" aria-label="Portrait of Diana Doe Jr" style="background:linear-gradient(160deg,#6e6e6e,#4a4440 55%,#2a3348)"></div>
    <h3 class="member__name">DIANA DOE JR</h3>
    <div class="member__rule"></div>
    <p class="member__role">Curabitur metus ligula</p>
  </article>
  <article class="member" style="left:831px">
    <div class="member__photo" role="img" aria-label="Portrait of Sarah Doe" style="background:linear-gradient(160deg,#a7ac9c,#c2c4b0 45%,#4f77a6 80%)"></div>
    <h3 class="member__name">SARAH DOE</h3>
    <div class="member__rule"></div>
    <p class="member__role">Curabitur metus ligula</p>
  </article>
</section>

<section class="testimonials">
  <p class="eyebrow testimonials__eyebrow">TESTIMONIALS</p>
  <h2 class="section-title testimonials__title">Clients say about us</h2>
</section>

</body>
</html>
```